Sir Pemberly's Keepsake Book cover

I need a paperback book cover, front, spine and back for a historical romance novel to be self-published on Quillmart.com.

I like clean, professional designs. I’d like something centered around the images of roses, diamonds, and/or a manor house.

About the book- Set 1819, Harriet Fenwicke leaves her brother’s house when her sister-in-law rips out her beloved rose garden to take a job as governess to the three wards of Silas Thornbury, the Earl of Pemberly. Silas is known as the most notorious rake tonnish society can boast of. Silas deeply in debt and is going to lose his family’s estate and manor house unless he can locate the lost treasure of the Pemberlys- A fabulous necklace formed by diamonds in the shape of roses. While solving riddles to find the treasure and dodging whoever is trying to kill Silas, the two fall in love. But finding the necklace proves easier than figuring how to make it work between the proper governess and the roguish earl.

Info for the cover:
Sir Pemberly’s Keepsake
Book 1 The Lantern Placement Bureau
Marcy Dawn Cullen

Text for the back:

Just when she thinks she is out of options, respectable Miss Harriet Fenwicke receives a mysterious letter offering her employment as governess to the three wards of the roguish Earl of Pemberly.

When he thinks he’s about to lose his family’s estate to debt, Silas Thornbury, Earl of Pemberly, returns home to find the lost treasure of the Pemberlys, a fabulous diamond necklace.

Together they search Pemberly Manor for the necklace, but solving the clues left by a feisty ancestress proves easier than fighting the passion between them.

Hi all, I'm still looking for designs.. In response to a couple of questions I've gotten: The title of the novel is: Sir Pemberly's Keepsake I'm looking for a standard sized paperback book cover, spine and back. For examples covers similar to what I have in mind please see these covers: http://www.quillmart-example.com/Heart-Fitting-Suitor-Rosalind-Harcourt-ebook/dp/Q000XK7TRW/ref=sr_1_11?s=books&ie=UTF8&qid=1498227104&sr=1-11&keywords=rosalind+harcourt and http://www.quillmart-example.com/Dukes-Sweetheart-Rosalind-Harcourt-ebook/dp/Q000XK8MNS/ref=sr_1_13?s=books&ie=UTF8&qid=1498227305&sr=1-13&keywords=rosalind+harcourt

```html
<!DOCTYPE html>
<html lang="en">
<head>
<meta charset="utf-8">
<title>Sir Pemberly’s Keepsake — Book Cover</title>
<link href="https://fonts.googleapis.com/css2?family=Archivo+Narrow:wght@400;500;600&family=Archivo:wght@500;600&display=swap" rel="stylesheet">
<style>
  :root {
    --sky: #ffffff;
    --aqua-light: #bff3ef;
    --aqua: #22c9c1;
    --teal: #12958b;
    --teal-deep: #073a35;
    --rose: #f0146f;
    --ink: #111111;
    --numeral: #a9a9a9;
    --numeral-side: #d98aa9;
    --rule: #5f6d6b;
  }
  html, body {
    margin: 0;
    padding: 0;
    overflow: hidden;
    background: #ffffff;
  }
  .cover {
    position: relative;
    width: 900px;
    height: 1200px;
    overflow: hidden;
    background: linear-gradient(to bottom,
      var(--sky) 0%,
      var(--sky) 6%,
      var(--aqua-light) 16%,
      var(--aqua) 36%,
      var(--aqua) 50%,
      var(--teal) 72%,
      var(--teal-deep) 100%);
    font-family: "Archivo Narrow", "Arial Narrow", sans-serif;
  }
  .series-title {
    position: absolute;
    top: 140px;
    left: 84px;
    width: 752px;
    height: 90px;
    margin: 0;
  }
  .series-title text {
    font-family: "Archivo Narrow", sans-serif;
    font-weight: 500;
    font-size: 74px;
    fill: var(--rose);
  }
  .novel-rule {
    position: absolute;
    top: 262px;
    left: 0;
    width: 900px;
    height: 16px;
  }
  .novel-label {
    position: absolute;
    top: 258px;
    left: 372px;
    width: 92px;
    text-align: center;
    font-family: "Archivo", sans-serif;
    font-size: 22px;
    line-height: 1;
    color: var(--rose);
  }
  .book-label {
    position: absolute;
    top: 345px;
    left: 158px;
    font-family: "Archivo", sans-serif;
    font-weight: 500;
    font-size: 106px;
    line-height: 1;
    color: var(--ink);
    letter-spacing: 6px;
  }
  .book-number {
    position: absolute;
    top: 326px;
    left: 446px;
    font-family: "Archivo", sans-serif;
    font-weight: 600;
    font-size: 190px;
    line-height: 1;
    color: var(--numeral);
    text-shadow:
      2px 2px 0 var(--numeral-side),
      4px 4px 0 var(--numeral-side),
      6px 6px 0 #c7c7c7;
  }
  .book-article {
    position: absolute;
    top: 498px;
    left: 88px;
    font-family: "Archivo", sans-serif;
    font-weight: 500;
    font-size: 74px;
    line-height: 1;
    color: var(--ink);
  }
  .book-title {
    position: absolute;
    top: 548px;
    left: 29px;
    width: 842px;
    height: 130px;
    margin: 0;
  }
  .book-title text {
    font-family: "Archivo Narrow", sans-serif;
    font-weight: 500;
    font-size: 130px;
    fill: var(--rose);
  }
  .author {
    position: absolute;
    top: 884px;
    left: 403px;
    width: 466px;
    text-align: center;
    font-family: "Archivo", sans-serif;
    font-weight: 500;
    font-size: 55px;
    line-height: 1;
    color: var(--ink);
    white-space: nowrap;
  }
  .author-rule {
    position: absolute;
    top: 954px;
    left: 396px;
    width: 480px;
    height: 14px;
  }
</style>
</head>
<body>
  <main class="cover">
    <h1 class="series-title">
      <svg viewBox="0 0 752 90" width="752" height="90">
        <text x="0" y="72" textLength="752" lengthAdjust="spacingAndGlyphs">Sir Pemberly’s Keepsake</text>
      </svg>
    </h1>

    <svg class="novel-rule" viewBox="0 0 900 16" aria-hidden="true">
      <g stroke="var(--rule)" stroke-width="2">
        <line x1="53" y1="5" x2="372" y2="5"/>
        <line x1="53" y1="11" x2="372" y2="11"/>
        <line x1="463" y1="5" x2="845" y2="5"/>
        <line x1="463" y1="11" x2="845" y2="11"/>
      </g>
    </svg>
    <div class="novel-label">A Novel</div>

    <div class="book-label">Book</div>
    <div class="book-number">1</div>

    <div class="book-article">The</div>
    <h2 class="book-title">
      <svg viewBox="0 0 842 130" width="842" height="130">
        <text x="0" y="104" textLength="842" lengthAdjust="spacingAndGlyphs">Lantern Placement Bureau</text>
      </svg>
    </h2>

    <div class="author">Marcy Dawn Cullen</div>
    <svg class="author-rule" viewBox="0 0 480 14" aria-hidden="true">
      <line x1="0" y1="3" x2="480" y2="3" stroke="#2d3b39" stroke-width="3"/>
      <line x1="0" y1="10" x2="480" y2="10" stroke="#7fa9a4" stroke-width="2"/>
    </svg>
  </main>
</body>
</html>
```